" atendimento domiciliar individual, avaliação antropométrica e diagnóstico nutricional, prescrição de dietas, acompanhamento do cliente por email e aplicativo "

```html
<!DOCTYPE html>
<html lang="pt-BR">
<head>
<meta charset="utf-8">
<title>Cartão de visita – Nutrição Clínica</title>
<link rel="stylesheet" href="https://fonts.googleapis.com/css2?family=Open+Sans:wght@400;600&display=swap">
<style>
  :root {
    --page-bg: #ecebe8;
    --card-bg: #ffffff;
    --ink-dark: #4a4540;
    --sage: #7fa37c;
    --sage-soft: #a9c3a2;
    --sage-pale: #d6e4d0;
    --shadow: rgba(0, 0, 0, 0.14);
  }
  * { box-sizing: border-box; margin: 0; padding: 0; }
  html, body {
    width: 1200px;
    height: 1200px;
    overflow: hidden;
    background: var(--page-bg);
    font-family: "Open Sans", sans-serif;
  }
  .sheet {
    position: relative;
    width: 1200px;
    height: 1200px;
  }
  .card {
    position: absolute;
    left: 220px;
    width: 760px;
    height: 420px;
    background: var(--card-bg);
    border-radius: 38px;
    box-shadow: 0 10px 30px var(--shadow);
    overflow: hidden;
  }
  .card--front { top: 150px; }
  .card--back { top: 630px; }

  /* Front */
  .brand {
    position: absolute;
    left: 0; right: 0;
    top: 50%;
    transform: translateY(-50%);
    display: flex;
    align-items: center;
    justify-content: center;
    gap: 22px;
  }
  .brand__dot {
    width: 46px;
    height: 46px;
    border-radius: 50%;
    background: var(--sage);
    flex: none;
  }
  .brand__text { display: flex; flex-direction: column; }
  .brand__name {
    font-weight: 600;
    font-size: 34px;
    letter-spacing: 0.5px;
    color: var(--ink-dark);
    line-height: 1.1;
  }
  .brand__field {
    margin-top: 8px;
    font-size: 15px;
    letter-spacing: 7px;
    color: var(--sage);
    text-transform: uppercase;
  }

  /* Back */
  .back-art {
    position: absolute;
    left: 0; top: 0;
    width: 300px;
    height: 420px;
    background: linear-gradient(160deg, var(--sage-soft) 0%, var(--sage-pale) 100%);
  }
  .contact {
    position: absolute;
    right: 46px;
    top: 62px;
    text-align: right;
    color: var(--sage);
  }
  .contact__name { font-size: 27px; line-height: 1.2; }
  .contact__role { font-size: 25px; line-height: 1.2; margin-bottom: 10px; }
  .contact__line {
    display: flex;
    justify-content: flex-end;
    align-items: center;
    gap: 10px;
    font-size: 22px;
    line-height: 1.45;
  }
  .contact__line--plain { padding-right: 32px; }
  .contact__icon { width: 22px; height: 22px; flex: none; fill: var(--sage); }
</style>
</head>
<body>
<main class="sheet">

  <section class="card card--front" aria-label="Frente do cartão">
    <div class="brand">
      <span class="brand__dot"></span>
      <div class="brand__text">
        <span class="brand__name">HELENA DUARTE MOREIRA</span>
        <span class="brand__field">Nutrição Clínica</span>
      </div>
    </div>
  </section>

  <section class="card card--back" aria-label="Verso do cartão">
    <div class="back-art" role="img" aria-label="Decorative sage-green leaf sweep with curved lines"></div>

    <div class="contact">
      <p class="contact__name">Nome Sobrenome</p>
      <p class="contact__role">Função</p>
      <p class="contact__line">contato@contato.com
        <svg class="contact__icon" viewBox="0 0 24 24"><path d="M2 5h20v14H2z M2 5l10 8 10-8" fill="var(--sage)" stroke="#fff" stroke-width="1.6"/></svg>
      </p>
      <p class="contact__line">(00)0000-0000
        <svg class="contact__icon" viewBox="0 0 24 24"><path d="M6.6 10.8a15 15 0 0 0 6.6 6.6l2.2-2.2c.3-.3.7-.4 1-.2 1.1.4 2.3.6 3.6.6.6 0 1 .4 1 1V20c0 .6-.4 1-1 1A17 17 0 0 1 3 4c0-.6.4-1 1-1h3.5c.6 0 1 .4 1 1 0 1.3.2 2.5.6 3.6.1.3 0 .7-.2 1z"/></svg>
      </p>
      <p class="contact__line">(00)0000-0000
        <svg class="contact__icon" viewBox="0 0 24 24"><circle cx="12" cy="12" r="10"/><path d="M8.5 7.5c.6 3.5 3 6.5 7 8l1.3-1.6-2-1-1 1c-1.5-.7-2.8-2-3.4-3.4l1-1-1-2z" fill="#fff"/></svg>
      </p>
      <p class="contact__line">rua sem nome,00
        <svg class="contact__icon" viewBox="0 0 24 24"><path d="M12 2a7 7 0 0 0-7 7c0 5 7 13 7 13s7-8 7-13a7 7 0 0 0-7-7zm0 9.5A2.5 2.5 0 1 1 12 6.5a2.5 2.5 0 0 1 0 5z"/></svg>
      </p>
      <p class="contact__line contact__line--plain">Bairro Sem Nome</p>
      <p class="contact__line contact__line--plain">Cidade Sem Nome</p>
    </div>
  </section>

</main>
</body>
</html>
```